Business Card Design for Small Electrical Contractor

I need to update my business card into something a little more modern. We are a small electrical contracting company. We service domestic and commercial places around Sydney. We have 2 logo designs at the moment. I have uploaded both and 2 different sizes to work with.

Industry/Entity Type

Business

Contact Information for Business Card

Leo Hartigan
8/21-23 Birch Rd, Kelsworth 2087
t - (02) 9381 4720
m - 0427 815 903
E - info@hartiganelx.com.au
W - hartiganelx.com.au
ABN: 42 907 551 316

Font styles to use
Sans Serif

Requirements
Must have
• I would also like to see the below fit on somewhere aswell
• - Licensed Electrician
• - Level 2 (Cat 1 & 4)
• - Domestic
• - Commercial
• - Repairs and Installations
• - Data
Nice to have
• Try and keep similar colours as logo
Should not have
• No lightning bolts or light globes. Smart and professional please.

```html
<!DOCTYPE html>
<html lang="en">
<head>
<meta charset="utf-8">
<title>Hartigan Electrical – Business Card</title>
<link href="https://fonts.googleapis.com/css2?family=Open+Sans:wght@400;600&display=swap" rel="stylesheet">
<style>
  :root {
    --bg: #ece9e4;
    --teal: #1d6462;
    --teal-dark: #124846;
    --teal-light: #2b7a77;
    --gold: #f2ad2b;
    --white: #ffffff;
    --paper: #f6f6f5;
    --ink-soft: #e4efee;
  }
  * { box-sizing: border-box; margin: 0; padding: 0; }
  html, body { width: 1200px; height: 1023px; overflow: hidden; }
  body {
    background: var(--bg);
    font-family: "Open Sans", sans-serif;
    position: relative;
  }
  .card {
    position: absolute;
    left: 250px;
    width: 700px;
    height: 400px;
    border-radius: 18px;
    overflow: hidden;
    box-shadow: 0 6px 18px rgba(0,0,0,.18);
  }
  .card--front { top: 60px; background: var(--paper); }
  .card--back {
    top: 560px;
    background: radial-gradient(ellipse at 40% 35%, var(--teal-light), var(--teal) 55%, var(--teal-dark));
  }

  /* front */
  .front__brand {
    position: absolute; left: 0; right: 0; top: 0; height: 215px;
    display: flex; align-items: center; justify-content: center;
  }
  .brand-name {
    font-weight: 600;
    font-size: 40px;
    letter-spacing: 1px;
    color: var(--teal);
  }
  .front__band {
    position: absolute; left: 0; right: 0; bottom: 0; height: 185px;
    background: linear-gradient(180deg, var(--teal-light), var(--teal) 40%, var(--teal-dark));
  }
  .contact {
    position: absolute; left: 36px; bottom: 22px;
    color: var(--white); font-size: 15px; line-height: 23px;
  }
  .contact__name { color: var(--gold); font-weight: 600; font-size: 18px; margin-bottom: 2px; }
  .contact__row { display: flex; align-items: center; gap: 8px; }
  .contact__row svg { width: 13px; height: 13px; flex: none; }
  .contact__row--plain { padding-left: 21px; }
  .services {
    position: absolute; right: 30px; top: 20px;
    list-style: none; text-align: right;
    color: var(--ink-soft); font-size: 14px; line-height: 22px;
  }
  .services li::after {
    content: ""; display: inline-block; width: 5px; height: 5px;
    border-radius: 50%; background: var(--gold);
    margin-left: 10px; vertical-align: middle;
  }

  /* back */
  .back__brand {
    position: absolute; left: 0; right: 0; top: 130px;
    display: flex; flex-direction: column; align-items: center;
  }
  .back__brand .brand-name { color: var(--white); font-size: 46px; }
  .back__rule { width: 330px; height: 2px; background: var(--gold); margin-top: 12px; }
  .website {
    position: absolute; left: 0; right: 0; bottom: 70px; text-align: center;
    color: var(--white); font-size: 14px; letter-spacing: 5px;
  }
</style>
</head>
<body>
  <section class="card card--front">
    <div class="front__brand">
      <span class="brand-name">Hartigan Electrical</span>
    </div>
    <div class="front__band">
      <ul class="services">
        <li>Licensed Electrician</li>
        <li>Level 2 (Cat 1 &amp; 4)</li>
        <li>Domestic</li>
        <li>Commercial</li>
        <li>Repairs and Installations</li>
        <li>Data</li>
      </ul>
      <div class="contact">
        <p class="contact__name">Leo Hartigan</p>
        <p class="contact__row contact__row--plain">8/21-23 Birch Rd, Kelsworth 2087</p>
        <p class="contact__row">
          <svg viewBox="0 0 14 14" aria-hidden="true"><rect x="1" y="4" width="12" height="9" rx="1.5" fill="var(--gold)"/><path d="M3 4 Q7 0 11 4" stroke="var(--gold)" stroke-width="2" fill="none"/></svg>
          (02) 9381 4720
        </p>
        <p class="contact__row">
          <svg viewBox="0 0 14 14" aria-hidden="true"><rect x="3.5" y="0.5" width="7" height="13" rx="1.2" fill="none" stroke="var(--white)" stroke-width="1.2"/><circle cx="7" cy="11.3" r=".9" fill="var(--white)"/></svg>
          0427 815 903
        </p>
        <p class="contact__row">
          <svg viewBox="0 0 14 14" aria-hidden="true"><rect x="1" y="3" width="12" height="8.5" rx="1" fill="var(--gold)"/><path d="M1.5 3.5 L7 8 L12.5 3.5" stroke="var(--teal)" stroke-width="1.2" fill="none"/></svg>
          info@hartiganelx.com.au
        </p>
        <p class="contact__row contact__row--plain">ABN: 42 907 551 316</p>
      </div>
    </div>
  </section>

  <section class="card card--back">
    <div class="back__brand">
      <span class="brand-name">Hartigan Electrical</span>
      <span class="back__rule"></span>
    </div>
    <p class="website">www.hartiganelx.com.au</p>
  </section>
</body>
</html>
```